"Every Lantern Still Burning" Sermon Series Design

Needing a design for our church's next sermon series titled "Every Lantern Still Burning" where we will discuss the need for unity, diversity, love and clarity. Looking for a 1920 x 1080 (or higher res) editable and layered file (PSD or AI) so that we can reformat the design to work on social, screens, lower thirds and various print and online mediums. We will also need to have access to the font files so that we can make resize and tweak as needed. We like the idea of using a globe or map of the world as the backdrop with the words overtop. Or, the idea of creating a bunch of newspaper clippings (generic, so that they can't actually be read) and making the shape of a heart. See attached examples. This website will give you an idea of our previous sermon series designs so you can have an idea of our style (but, feel free to help us advance the ball on something more aligned with current design trends): https://www.brinmoorfellowship.church/series

Examples use red, but stay away from a ton of red. If you're gonna major in a color, use blue or something in that family.

Must haves:
Title: Every Lantern Still Burning
Tagline : (TBD - use some Lorem Ipsum as a placeholder and we will fill in later)
Our Logo (attached) (small towards bottom is standard - only use solid colors for logo - preferably just solid black or white)

Industry/Entity Type

Church

Font styles to use
Serif
Sans Serif

Requirements
Must have
• Title: Every Lantern Still Burning
Nice to have
• We like the idea of using a globe or map of the world as the backdrop with the words overtop. Or, the idea of creating a bunch of newspaper clippings (generic, so that they can't actually be read) and making the shape of a heart. See attached examples.

If you're gonna major on a color, stick with blue or something close.
Should not have
• Don't use red as the primary color (example we sent has red, but stay away from it)

```html
<!DOCTYPE html>
<html lang="en">
<head>
<meta charset="utf-8">
<title>Every Lantern Still Burning — Sermon Series</title>
<link rel="stylesheet" href="https://fonts.googleapis.com/css2?family=Jost:wght@500;600&display=swap">
<style>
  :root {
    --page: #ffffff;
    --ink: #0d2a40;
    --frame: #2c3f5a;
    --glow: #05a8e8;
    --mid: #3b86c6;
    --edge: #4a72b3;
    --corner: #43618a;
    --land: rgba(40, 70, 110, 0.32);
  }
  * { box-sizing: border-box; margin: 0; padding: 0; }
  html, body {
    width: 1200px;
    height: 796px;
    overflow: hidden;
    background: var(--page);
  }
  .canvas {
    position: relative;
    width: 1200px;
    height: 796px;
    background: var(--page);
  }
  .series-card {
    position: absolute;
    left: 139px;
    top: 139px;
    width: 925px;
    height: 521px;
    border: 0.5px solid var(--frame);
    overflow: hidden;
    background:
      radial-gradient(ellipse 62% 68% at 50% 50%, var(--glow) 0%, #1e92d6 38%, var(--mid) 62%, var(--edge) 82%, var(--corner) 100%);
  }
  .world-map {
    position: absolute;
    left: 116px;
    top: 133px;
    width: 682px;
    height: 273px;
    border-radius: 48% 48% 30% 30% / 60% 60% 40% 40%;
    background: radial-gradient(ellipse 50% 50% at 50% 45%, var(--land) 0%, rgba(40, 70, 110, 0.22) 55%, rgba(40, 70, 110, 0) 100%);
  }
  .series-title {
    position: absolute;
    left: 0;
    right: 0;
    top: 186px;
    text-align: center;
    font-family: "Jost", "Futura", sans-serif;
    font-weight: 600;
    font-size: 28px;
    line-height: 59px;
    color: var(--ink);
    text-transform: uppercase;
  }
  .series-title span {
    display: block;
    letter-spacing: 0.95em;
    padding-left: 0.95em;
  }
  .church-mark {
    position: absolute;
    left: 0;
    right: 0;
    top: 435px;
    display: flex;
    justify-content: center;
    align-items: center;
    gap: 8px;
    font-family: "Jost", "Futura", sans-serif;
    font-weight: 600;
    font-size: 11px;
    letter-spacing: 0.18em;
    text-transform: uppercase;
    color: var(--ink);
  }
  .church-mark svg { display: block; }
</style>
</head>
<body>
  <main class="canvas">
    <section class="series-card">
      <div class="world-map" role="img" aria-label="Dotted map of the world's continents"></div>
      <h1 class="series-title">
        <span>Every</span>
        <span>Lantern Still</span>
        <span>Burning</span>
      </h1>
      <div class="church-mark">
        <svg width="20" height="20" viewBox="0 0 20 20" aria-hidden="true">
          <circle cx="10" cy="10" r="8.5" fill="none" stroke="currentColor" stroke-width="1.6"/>
        </svg>
        <span>Brinmoor Fellowship</span>
      </div>
    </section>
  </main>
</body>
</html>
```